Flyer-Design für Karin Dossow
Zielgruppe
Ich bin psychologische Beraterin und Heilpraktikerin für Psychotherapie. Ich biete ein Coaching speziell für Mütter (meist Mütter mit neugeborenen Babys) an. Dieses Mütter-Coaching will ich bewerben. Die Flyer werden unter anderen an Ärzte und Hebammen weiter gegeben und dort in den Praxen ausliegen.
Aufgabenstellung
In meinem Logo herrschen die Farben orange und grau vor - es wäre schön, wenn sich diese Farben im Flyer wiederfinden würden - evtl. kombiniert mit mittelblau oder einem hellem grün.
Des weiteren möchte ich später Flyer im Din Lang Format (einseitig) mit anderen Angeboten erstellen. Das sollte mit dem Design dann auch möglich sein.
Der Schrifttyp soll bitte Arial sein, passend zum Logo. Ich habe bei Bildarko Fotos zu dem Thema erstanden, die ich stimmig finde. Diese Bilder sollten im Flyer genutzt werden.
Für diesen Flyer hätte ich gerne das Format: Falzblatt mit Wickelfalz - 279 x 219 mm

```html
<!DOCTYPE html>
<html lang="de">
<head>
<meta charset="utf-8">
<title>Karin Dossow – Coaching für Mütter</title>
<link href="https://fonts.googleapis.com/css2?family=Arimo:wght@400;700&family=Roboto:wght@500;700&display=swap" rel="stylesheet">
<style>
  :root {
    --green: #8a8c45;
    --orange: #ef9b35;
    --orange-text: #ef8f22;
    --blue: #1e66a0;
    --grey-head: #7a7a7a;
    --grey-text: #3f3f3f;
    --grey-panel: #efedeb;
    --white: #ffffff;
    --photo-light: #e6e2d8;
    --photo-dark: #3a2c28;
  }
  * { margin: 0; padding: 0; box-sizing: border-box; }
  html, body { width: 1200px; height: 851px; overflow: hidden; background: var(--white); }
  body { font-family: "Arimo", Arial, sans-serif; color: var(--grey-text); }
  .flyer { position: relative; width: 1200px; height: 851px; }

  .band { position: absolute; top: 0; height: 200px; color: var(--white); text-align: center; }
  .band::after {
    content: ""; position: absolute; bottom: -16px;
    border-left: 16px solid transparent; border-right: 16px solid transparent;
    border-top: 16px solid currentColor;
  }
  .band--green { left: 0; width: 393px; background: var(--green); }
  .band--green::after { left: 60px; border-top-color: var(--green); }
  .band--orange { left: 393px; width: 402px; background: var(--orange); }
  .band--orange::after { left: 185px; border-top-color: var(--orange); }
  .band--blue { left: 795px; width: 405px; background: var(--blue); z-index: 2; }
  .band--blue::after { left: 54px; border-top-color: var(--blue); }

  .why { font-family: "Roboto", Arial, sans-serif; font-weight: 700; padding-top: 45px; line-height: 1.2; }
  .why__q { font-size: 25px; }
  .why__a { font-size: 21px; margin-top: 2px; }

  .brand { font-family: "Arimo", Arial, sans-serif; font-size: 34px; color: var(--grey-head); letter-spacing: -0.5px; display: inline-flex; align-items: center; gap: 8px; }
  .brand__dot { width: 12px; height: 12px; border-radius: 50%; background: var(--orange); }
  .band--orange .brand { margin-top: 60px; color: var(--white); }
  .band--orange .brand__dot { background: var(--white); }
  .tagline__title { font-size: 21px; font-weight: 700; color: #6f6f6f; margin-top: 14px; }
  .tagline__sub { font-size: 19px; color: #555; margin-top: 6px; }

  .quote { font-family: "Roboto", Arial, sans-serif; font-weight: 700; font-size: 26px; line-height: 1.33; padding-top: 72px; }
  .quote__mark { position: absolute; font-size: 44px; line-height: 1; }
  .quote__mark--open { left: 55px; top: 72px; }
  .quote__mark--close { right: 62px; top: 142px; }

  .col-left { position: absolute; left: 17px; top: 290px; width: 365px; font-size: 14.5px; line-height: 22.5px; }
  .col-left h2 { font-size: 20px; color: var(--grey-head); text-align: center; margin-bottom: 33px; }
  .col-left h2 span { color: var(--orange-text); }
  .col-left p { margin-bottom: 22.5px; }

  .offers { position: absolute; left: 412px; top: 230px; width: 360px; font-size: 14.5px; line-height: 22.5px; color: #555; }
  .offers p { margin-bottom: 22.5px; }
  .offers b { font-weight: 400; color: var(--orange-text); font-size: 16px; }

  .contact { position: absolute; left: 393px; top: 515px; width: 402px; height: 318px; background: var(--grey-panel); text-align: center; font-size: 14.5px; line-height: 22.5px; color: #444; padding-top: 20px; }
  .contact::before { content: ""; position: absolute; top: 0; left: 186px; border-left: 15px solid transparent; border-right: 15px solid transparent; border-top: 15px solid var(--white); }
  .contact__name { font-size: 18px; line-height: 28px; margin-top: 2px; }
  .contact__gap { height: 22px; }

  .photo { position: absolute; left: 795px; top: 200px; width: 405px; height: 417px; background: linear-gradient(90deg, var(--photo-light) 0%, #d9cfc6 45%, var(--photo-dark) 100%); }
  .brand-block { position: absolute; left: 795px; top: 652px; width: 405px; text-align: center; }

  .foot { position: absolute; bottom: 0; height: 18px; }
  .foot--green { left: 0; width: 393px; background: var(--green); }
  .foot--orange { left: 393px; width: 402px; background: var(--orange); }
  .foot--blue { left: 795px; width: 405px; background: var(--blue); }
</style>
</head>
<body>
<main class="flyer">
  <header class="band band--green why">
    <div class="why__q">Warum Coaching<br>extra für Mütter?</div>
    <div class="why__a">Nur wer gut für sich selbst sorgt,<br>kann auch für andere da sein!</div>
  </header>

  <header class="band band--orange">
    <div class="brand"><span>karindossow</span><span class="brand__dot"></span></div>
    <div class="tagline__title">Coaching für Mütter</div>
    <div class="tagline__sub">Begleitung - Stärkung - Beratung</div>
  </header>

  <header class="band band--blue quote">
    <span class="quote__mark quote__mark--open">”</span>
    Das Baby ist da<br>und nichts ist mehr<br>wie es war
    <span class="quote__mark quote__mark--close">“</span>
  </header>

  <section class="col-left">
    <h2>Coaching <span>für Mütter</span></h2>
    <p>Als Heilpraktikerin für Psychotherapie und geprüfte psychologische Beraterin habe ich mich besonders auf das Coaching für Mütter spezialisiert.</p>
    <p>Ich setzte dabei die Methode des lösungsorientierten Kurzzeitcoachings ein, das den <strong>Fokus auf Stärken und Lösungen</strong> legt und nicht die Probleme und Hindernisse in den Vordergrund stellt.</p>
    <p>Das Konzept wird durch Achtsamkeits- und Entspannungsübungen abgerundet. Aspekte der gewaltfreien“ = wertschätzenden Kommunikation werden für individuelle Konfliktlösungen im familiären Alltag genutzt.</p>
    <p><strong>Starten Sie mit einem neuen und liebevollen Blick auf Ihr Leben und auf Ihre Fähigkeiten.</strong></p>
    <p>Sie werden erstaunt sein, was alles in Ihnen wohnt</p>
  </section>

  <section class="offers">
    <p><b>Einzelcoaching</b> Sie können wählen: das Coaching kann in meiner Praxis in Hilden oder gern auch bei Ihnen zu Hause stattfinden, allein oder mit Partner, so wie es gerade für Sie am besten passt.</p>
    <p><b>Gruppencoaching</b> Lernen Sie Gleichgesinnte kennen und profitieren Sie in doppelter Hinsicht – nach dem Motto: „Lieber gemeinsam als einsam“.</p>
    <p><b>TelefonCoaching</b> Sie bestimmen Ort und Zeit. Dieses Angebot könnte das Richtige für Sie sein, wenn Sie zeitlich oder örtlich gebunden sind.</p>
  </section>

  <address class="contact" style="font-style:normal">
    Rufen Sie mich doch einfach unverbindlich an<br>- ich freue mich auf Sie!
    <div class="contact__name">Karin Dossow</div>
    Heilpraktikerin für Psychotherapie<br>Geprüfte Psychologische Beraterin
    <div class="contact__gap"></div>
    Telefon: 0160 482 31 706<br>Email: info@karin-dossow.de<br>www.karin-dossow.de
    <div class="contact__gap"></div>
    Praxisgemeinschaft am Hain<br>Dachsweg 14b<br>40721 Hilden am Rhein
  </address>

  <div class="photo" role="img" aria-label="Foto: junge Mutter hält ihr schlafendes Neugeborenes an der Schulter"></div>

  <div class="brand-block">
    <div class="brand"><span>karindossow</span><span class="brand__dot"></span></div>
    <div class="tagline__title">Coaching für Mütter</div>
    <div class="tagline__sub">Begleitung - Stärkung - Beratung</div>
  </div>

  <div class="foot foot--green"></div>
  <div class="foot foot--orange"></div>
  <div class="foot foot--blue"></div>
</main>
</body>
</html>
```